Parallax site with a story.

Hi!

This project is to create a website for a restaurant.

Inspiration you can get from
http://www.holmvik-starbeck.example/catering/
http://www.tavu-restaurant.example/
http://www.corvelloartrestaurant.example/fine-dining/
http://www.elpuertoquinteria.example/lima/

I have written a pdf that is attached. Please read that for more info.

I would LOVE to have the website made witin parallax like this website: http://www.holmvik-starbeck.example/se/

I have made a preliminary logotype and drawed some pictures, how it can look. Is an example- you maybe can improve it if you think its needed.

I will be available 24/7 from now for any question about project.

Reason: The project has been to a slow start, so I am increasing the deadline time of the project. Thanks

Reason: Hi! Site has been a bit slow unfortunately - I will do the following. I will scetch up a new descrition of project which will involve much less animation. will come back with this tomorrow.

Hi!

Please see descpriton

Hi Everybody!

I have decided to wait with the pictures (page 6 in pdf) and focus on these parts:

1) Create a website with inspiration from the two websites i wrote about in description
2) http://vindrosen.7reserve.example/   I want to add bookingsystem like this. 
http://www.vindrosen.example/  (click "Boka" to see it live).
3) A contact form for visitors to post message that is sent to me. (name, number, company, text)

The past animation/parallax is totally replaced by this.  And

Reason: Because I need time to organize your work. I have understood that you have difficulties to understand my idea or vision. I have to givemore information to you, and that's why I'm extending the time.

35+ people with intesting in fine bistro dining.

Restaurant

• Nice design. See page 4 for example of artwork in photoshop needed.

Also system for booking a table, or booking catering also important
• It should not relate to "cheap tex mex".

```html
<!DOCTYPE html>
<html lang="en">
<head>
<meta charset="utf-8">
<title>Solvara Restaurant</title>
<link href="https://fonts.googleapis.com/css2?family=Quicksand:wght@400;500&display=swap" rel="stylesheet">
<style>
  :root {
    --page-bg: #ffffff;
    --panel: rgba(38, 28, 22, 0.66);
    --text: #ffffff;
    --rule: rgba(255, 255, 255, 0.7);
    --field: #ffffff;
    --field-hint: #b9b9b9;
    --button-top: #ffb21a;
    --button-bottom: #f58a00;
  }
  * { box-sizing: border-box; margin: 0; padding: 0; }
  html, body { width: 1200px; height: 895px; overflow: hidden; background: var(--page-bg); }
  body { position: relative; font-family: "Quicksand", sans-serif; color: var(--text); }

  .hero-photo {
    position: absolute; left: 0; top: 30px; width: 1200px; height: 835px;
    background:
      radial-gradient(ellipse at 85% 70%, rgba(214, 96, 30, 0.85), transparent 45%),
      radial-gradient(ellipse at 18% 30%, rgba(226, 160, 120, 0.8), transparent 50%),
      radial-gradient(ellipse at 90% 15%, rgba(230, 200, 150, 0.7), transparent 45%),
      linear-gradient(160deg, #c89a74 0%, #a8704a 40%, #7a4a2c 70%, #b86a32 100%);
  }

  .panel {
    position: absolute; left: 281px; top: 93px; width: 651px; height: 726px;
    background: var(--panel);
    box-shadow: 0 2px 6px rgba(0,0,0,0.35);
  }

  .contact-bar {
    position: absolute; top: 29px; left: 27px; right: 37px;
    display: flex; justify-content: space-between; align-items: center;
    font-size: 16px; font-weight: 500;
  }
  .contact-bar span { display: flex; align-items: center; gap: 6px; }

  .brand {
    position: absolute; top: 152px; left: 0; width: 100%;
    display: flex; justify-content: center; align-items: center; gap: 12px;
    font-size: 34px; font-weight: 500; letter-spacing: 0.5px;
  }
  .brand-dot { width: 14px; height: 14px; border-radius: 50%; background: var(--text); }

  .main-nav {
    position: absolute; top: 207px; left: 35px; right: 35px;
    border-top: 1px solid var(--rule);
    display: flex; justify-content: space-between;
    padding-top: 11px;
    font-size: 18.5px; letter-spacing: 0.6px;
  }

  .story {
    position: absolute; top: 303px; left: 36px; right: 36px;
    text-align: center; font-size: 16px; line-height: 20px; font-weight: 500;
  }
  .story p + p { margin-top: 42px; padding: 0 12px; }

  .field {
    position: absolute; height: 35px; background: var(--field);
    color: var(--field-hint); font-size: 15px;
    display: flex; align-items: center; justify-content: center;
  }
  .field-name { left: 192px; top: 521px; width: 261px; }
  .field-address { left: 150px; top: 568px; width: 345px; }

  .contact-button {
    position: absolute; left: 218px; top: 614px; width: 212px; height: 42px;
    background: linear-gradient(var(--button-top), var(--button-bottom));
    font-size: 26px; letter-spacing: 1px;
    display: flex; align-items: center; justify-content: center;
  }

  .slide-dots {
    position: absolute; top: 679px; left: 0; width: 100%;
    display: flex; justify-content: center; gap: 8px;
  }
  .slide-dots i {
    width: 14px; height: 14px; border-radius: 50%;
    border: 3px solid var(--text); background: rgba(0,0,0,0.3);
  }
</style>
</head>
<body>
  <div class="hero-photo" role="img" aria-label="Blurred photo of diners sharing a bistro meal with roasted dishes and glasses on a wooden table"></div>

  <main class="panel">
    <div class="contact-bar">
      <span>
        <svg width="22" height="14" viewBox="0 0 22 14"><rect x="0.5" y="0.5" width="21" height="13" fill="#fff"/><path d="M1 1 L11 8 L21 1" stroke="#3a2a20" stroke-width="1.5" fill="none"/></svg>
        contact@solvara.example
      </span>
      <span>
        <svg width="18" height="16" viewBox="0 0 18 16"><path d="M1 5 Q9 -1 17 5 L15 7 L12 5 L12 3 Q9 2 6 3 L6 5 L3 7 Z" fill="#fff"/><rect x="3" y="8" width="12" height="7" rx="1.5" fill="#fff"/><circle cx="9" cy="11.5" r="2" fill="#3a2a20"/></svg>
        ( 0283 ) 5550 184
      </span>
    </div>

    <div class="brand"><span class="brand-dot"></span>Solvara Restaurant</div>

    <nav class="main-nav">
      <span>HOME</span><span>ABOUT US</span><span>MENUS</span><span>OUR LOCATION</span><span>CONTACT</span>
    </nav>

    <section class="story">
      <p>The restaurant is beautifully decorated including fresh flowers on side tables and nice reproductions of paintings which make the place authentic to a good Parisian restaurant. For a while you feel like you were back in Europe and not in Vietnam!</p>
      <p>The food was tasty - I tried the fish of the day. For me the fish was a bit unsalty, but it cannot be a problem for others and can be easily solved.</p>
    </section>

    <div class="field field-name">name</div>
    <div class="field field-address">address</div>
    <div class="contact-button">CONTACT</div>

    <div class="slide-dots"><i></i><i></i><i></i></div>
  </main>
</body>
</html>
```